VELUNDO Brisbane Tiling Service

My name is Mirko Bostel i need a business card for a new company. We are wall and floor tilers based in Brisbane, our company is Velundio Brisbane Tiling Service.
We would like a logo from our website used on our cards. Our website is www.velundio.com.au

I would like my Facebook and Twitter accounts on my card.

Industry/Entity Type

Business

Colors
0692cd
3176b5
33a6d7
85cae6

```html
<!DOCTYPE html>
<html lang="en">
<head>
<meta charset="utf-8">
<title>Velundio Brisbane Tiling Service – Business Card</title>
<link rel="stylesheet" href="https://fonts.googleapis.com/css2?family=Arimo:wght@400&display=swap">
<style>
  :root {
    --brand-blue: #0692cd;
    --brand-blue-deep: #3176b5;
    --brand-blue-mid: #33a6d7;
    --brand-blue-light: #85cae6;
    --card-white: #ffffff;
    --card-tint: #eef0f2;
    --stage: #2b2b2d;
    --text-light: #ffffff;
  }
  * { box-sizing: border-box; margin: 0; padding: 0; }
  html, body {
    width: 1200px;
    height: 900px;
    overflow: hidden;
    background: var(--stage);
    font-family: "Arimo", Arial, sans-serif;
  }
  .card {
    position: absolute;
    left: 320px;
    width: 560px;
    height: 320px;
    overflow: hidden;
    background: linear-gradient(135deg, var(--card-white) 0%, var(--card-tint) 100%);
    box-shadow: 0 10px 30px rgba(0, 0, 0, 0.5);
  }
  .card-front { top: 100px; }
  .card-back { top: 480px; }

  /* Front */
  .brand-lockup {
    position: absolute;
    left: 44px;
    top: 176px;
    display: flex;
    align-items: flex-end;
    gap: 14px;
  }
  .brand-square {
    width: 82px;
    height: 82px;
    border-radius: 6px;
    background: var(--brand-blue-deep);
  }
  .brand-text { display: flex; flex-direction: column; line-height: 1; }
  .brand-name {
    font-size: 62px;
    color: var(--brand-blue-deep);
    letter-spacing: 0.5px;
  }
  .brand-tagline {
    margin-top: 4px;
    font-size: 24px;
    color: var(--brand-blue-deep);
  }

  /* Back */
  .info-band {
    position: absolute;
    left: 0;
    right: 0;
    top: 110px;
    height: 116px;
    background: var(--brand-blue);
    display: flex;
    align-items: center;
  }
  .band-mark {
    width: 62px;
    height: 62px;
    margin-left: 126px;
    background: var(--card-tint);
  }
  .band-divider {
    width: 2px;
    height: 84px;
    margin-left: 92px;
    background: rgba(255, 255, 255, 0.85);
  }
  .contact {
    margin-left: 40px;
    color: var(--text-light);
  }
  .contact-name {
    font-size: 25px;
    letter-spacing: 0.5px;
    margin-bottom: 10px;
  }
  .contact-list { list-style: none; font-size: 13px; line-height: 17px; }
  .contact-list li { display: flex; align-items: center; gap: 8px; }
  .contact-list svg { width: 10px; height: 10px; fill: var(--text-light); }
</style>
</head>
<body>
  <section class="card card-front" aria-label="Card front">
    <div class="brand-lockup">
      <div class="brand-square"></div>
      <div class="brand-text">
        <span class="brand-name">velundio</span>
        <span class="brand-tagline">brisbane tiling service</span>
      </div>
    </div>
  </section>

  <section class="card card-back" aria-label="Card back">
    <div class="info-band">
      <div class="band-mark"></div>
      <div class="band-divider"></div>
      <div class="contact">
        <p class="contact-name">Mirko Bostel</p>
        <ul class="contact-list">
          <li>
            <svg viewBox="0 0 10 10" aria-hidden="true"><path d="M2 0.5 L3.6 2.6 L2.8 3.6 Q4 6 6.4 7.2 L7.4 6.4 L9.5 8 L8.4 9.5 Q2.5 9 0.5 1.6 Z"/></svg>
            0400 555 018
          </li>
          <li>
            <svg viewBox="0 0 10 10" aria-hidden="true"><path d="M0.5 2 H9.5 V8 H0.5 Z M1.2 2.6 L5 5.4 L8.8 2.6" fill="none" stroke="#fff" stroke-width="1"/></svg>
            info@velundio.com.au
          </li>
          <li>
            <svg viewBox="0 0 10 10" aria-hidden="true"><path d="M5 0.8 L9.5 5 H8 V9.2 H6 V6.5 H4 V9.2 H2 V5 H0.5 Z"/></svg>
            www.velundio.com.au
          </li>
        </ul>
      </div>
    </div>
  </section>
</body>
</html>
```